Home show booth design

We are looking at a home show booth design for our window and door company. We will have some high end doors, windows, patio door and garage door on display. 1 booth is 10x20 and 1 booth is 20x20.

Give me some design ideas and keeping in mind our product on display.

Below is our logo and i would like to keep our branding colors and i want a very attractive and high end setup to stand out from the crowd

Target Market(s)

Home owners and custom home builders

Industry/Entity Type

Windows and doors

Font styles to use
Serif

Colors

Designer to choose colors to be used in the design.

Requirements
Must have
• Back drop, small desk
Nice to have
• Large floating balloon above the booth

```html
<!DOCTYPE html>
<html lang="en">
<head>
<meta charset="utf-8">
<title>Keystone Doors &amp; Windows – Home Show Booth</title>
<link rel="stylesheet" href="https://fonts.googleapis.com/css2?family=Roboto:wght@900&family=Poppins:wght@400;500;600;700&display=swap">
<style>
  :root {
    --orange: #e0701c;
    --rust: #c5461c;
    --charcoal: #3b3730;
    --espresso: #2a241c;
    --black: #1c1b1a;
    --white: #ffffff;
    --stage: #d3d3d3;
    --counter-top: #7a7875;
  }
  * { box-sizing: border-box; margin: 0; padding: 0; }
  html, body { width: 1200px; height: 840px; overflow: hidden; }
  body { background: var(--stage); position: relative; font-family: "Poppins", sans-serif; }

  /* ---------- Brand lockup ---------- */
  .brand { position: absolute; font-family: "Roboto", sans-serif; font-weight: 900; }
  .brand-mark { position: absolute; background: var(--charcoal); border-radius: 4px; }
  .brand-name { position: absolute; display: block; line-height: 1; }
  .brand-tag { position: absolute; display: block; line-height: 1; letter-spacing: 0.04em; }

  /* ---------- Backwall ---------- */
  .backwall {
    position: absolute; left: 470px; top: 100px; width: 660px; height: 640px;
    background: var(--white); overflow: hidden;
  }
  .backwall .brand { left: 0; top: 0; width: 660px; height: 150px; color: var(--orange); }
  .backwall .brand-mark { left: 136px; top: 14px; width: 124px; height: 124px; }
  .backwall .brand-name { left: 277px; top: 42px; font-size: 47px; }
  .backwall .brand-tag  { left: 280px; top: 94px; font-size: 19px; }

  .headline {
    position: absolute; left: 25px; top: 154px; right: 10px;
    font-family: "Roboto", sans-serif; font-weight: 900; line-height: 42px;
  }
  .headline-lead { display: block; color: var(--orange); font-size: 48px; }
  .headline-name { display: block; color: var(--charcoal); font-size: 50px; }

  .services-tab {
    position: absolute; left: 0; top: 268px; width: 228px; height: 38px;
    background: var(--orange); color: var(--white);
    clip-path: polygon(0 0, 206px 0, 100% 100%, 0 100%);
    font-size: 26px; font-weight: 500; line-height: 40px; padding-left: 25px;
  }
  .services-tab strong { font-weight: 700; }
  .services-list {
    position: absolute; left: 27px; top: 316px; list-style: none;
    font-size: 21px; font-weight: 500; color: var(--espresso);
  }
  .services-list li { height: 33px; }
  .services-list li::before { content: "•"; color: var(--orange); margin-right: 9px; }

  .footer-band {
    position: absolute; left: 0; top: 506px; width: 232px; height: 134px;
    background: linear-gradient(100deg, var(--black) 10%, #3a2e22 100%);
    border-top: 5px solid var(--orange);
  }
  .web { font-family: "Poppins", sans-serif; font-weight: 600; color: #f1ece6; }
  .web span { color: var(--orange); }
  .footer-band .web { position: absolute; left: 27px; top: 46px; font-size: 19.5px; }

  .photo { position: absolute; }
  .photo-patio { left: 236px; top: 270px; width: 194px; height: 118px;
    background:
      linear-gradient(180deg, transparent 78%, #8a6646 78%, #6b4b32 100%),
      linear-gradient(90deg, #2b2b2e 0 16%, #7e8a9c 16%, #a6a6a0 50%, #8e9aa6 86%, #3a3f48 86%); }
  .photo-sunroom { left: 436px; top: 270px; width: 200px; height: 124px;
    background:
      linear-gradient(180deg, #f3f5f6 0%, #dfe8ec 48%, transparent 48%),
      linear-gradient(90deg, #8b6c4f 0%, #b9a387 40%, #c7c4bd 60%, #2f4258 80%, #4a5e74 100%); }
  .photo-house { left: 236px; top: 392px; width: 242px; height: 108px;
    background:
      linear-gradient(180deg, transparent 62%, #52704a 62%, #3f5a34 100%),
      linear-gradient(180deg, #435a8c 0%, #7b86a6 40%, #cdb79a 62%); }
  .photo-entry { left: 482px; top: 398px; width: 154px; height: 106px;
    background: linear-gradient(90deg, #f1f0ec 0 44%, #e2e1dc 44% 52%, #7f93a8 52% 74%, #f2f1ee 74% 90%, #c9ccd0 90%); }
  .photo-windows { left: 236px; top: 504px; width: 400px; height: 136px;
    background:
      linear-gradient(180deg, #5a3820 0 16%, transparent 16%),
      linear-gradient(100deg, #6d4a2c 0%, #a38a6e 30%, #c5b08e 55%, #8a7056 75%, #3d3129 100%); }

  .edge-strip { position: absolute; left: 641px; top: 0; width: 19px; height: 640px; background: var(--white); }
  .edge-strip::after {
    content: ""; position: absolute; left: 0; top: 533px; width: 19px; height: 107px;
    background: var(--black); border-top: 5px solid var(--rust);
  }

  /* ---------- Counter ---------- */
  .counter { position: absolute; left: 186px; top: 420px; width: 248px; height: 320px; }
  .counter-top { position: absolute; left: -8px; top: 0; width: 264px; height: 8px;
    background: var(--counter-top); border-radius: 4px 4px 0 0; }
  .counter-cap { position: absolute; left: 8px; top: 8px; width: 232px; height: 26px;
    background: var(--black); border-radius: 6px 6px 0 0; }
  .counter-face { position: absolute; left: 8px; top: 34px; width: 232px; height: 184px; background: var(--white); }
  .counter .brand { left: 0; top: 0; width: 232px; height: 184px; color: var(--rust); }
  .counter .brand-mark { left: 79px; top: 16px; width: 74px; height: 74px; }
  .counter .brand-name { left: 0; right: 0; top: 106px; text-align: center; font-size: 28px; }
  .counter .brand-tag  { left: 0; right: 0; top: 138px; text-align: center; font-size: 12px; }
  .counter-band { position: absolute; left: 8px; top: 218px; width: 232px; height: 52px;
    background: var(--espresso); border-top: 5px solid var(--rust); }
  .counter-band .web { position: absolute; left: 0; right: 0; top: 13px; text-align: center; font-size: 12.5px; }
  .counter-base { position: absolute; left: 8px; top: 270px; width: 232px; height: 50px;
    background: var(--black); border-radius: 0 0 8px 8px; }
</style>
</head>
<body>

  <section class="counter" aria-label="Reception counter wrap">
    <div class="counter-top"></div>
    <div class="counter-cap"></div>
    <div class="counter-face">
      <div class="brand">
        <span class="brand-mark"></span>
        <span class="brand-name">KEYSTONE</span>
        <span class="brand-tag">Doors &amp; Windows</span>
      </div>
    </div>
    <div class="counter-band"><p class="web">keystonedoors<span>.org</span></p></div>
    <div class="counter-base"></div>
  </section>

  <section class="backwall" aria-label="Booth backdrop">
    <div class="brand">
      <span class="brand-mark"></span>
      <span class="brand-name">KEYSTONE</span>
      <span class="brand-tag">Doors &amp; Windows</span>
    </div>

    <h1 class="headline">
      <span class="headline-lead">Elevate Your Home With</span>
      <span class="headline-name">Keystone Doors &amp; Windows</span>
    </h1>

    <h2 class="services-tab">Our <strong>Services</strong></h2>
    <ul class="services-list">
      <li>High end Doors</li>
      <li>Windows</li>
      <li>Patio Door and</li>
      <li>Garage Door</li>
    </ul>

    <div class="footer-band"><p class="web">keystonedoors<span>.org</span></p></div>

    <div class="photo photo-patio" role="img" aria-label="Family sitting behind a large glass patio door on a wooden deck"></div>
    <div class="photo photo-sunroom" role="img" aria-label="Bright sunroom lined with white-framed windows"></div>
    <div class="photo photo-house" role="img" aria-label="Two-storey home at dusk with lit windows and garage doors"></div>
    <div class="photo photo-entry" role="img" aria-label="Blue-grey front entry door with glass inset in a white hallway"></div>
    <div class="photo photo-windows" role="img" aria-label="Couple looking out through wood-framed windows at a lake view"></div>

    <div class="edge-strip"></div>
  </section>

</body>
</html>
```